Design a Coming Soon page for selling in Pixelbazaar

Do you want be part of our team and help us to design a professional Coming Soon page?
Do you want we share your design in Pixelbazaar? and share your name as designer there?

We have plan to create a professional HTML coming soon pages and sell it in Pixelbazaar!
for now we need a professional and elegant mock-up for it. NO COPY PASTE MOCK-UP
We want to compete with most popular web designers that created a html coming soon page before, example::
http://pixelbazaar-demo.net/item/zelkor-responsive-coming-soon-page/5172630
and we need better designs then our above competitor!
so if you can create a professional coming soon mock-up then provide your entry here and win the prize
Note: this contest will have multiple winner!

```html
<!DOCTYPE html>
<html lang="en">
<head>
<meta charset="utf-8">
<title>Darvelle — Coming soon</title>
<link rel="stylesheet" href="https://fonts.googleapis.com/css2?family=Arimo:wght@400;700&family=Dancing+Script:wght@400&display=swap">
<style>
  :root {
    --brand-red: #d9290a;
    --accent-red: #e0101c;
    --ring-red: #d5101c;
    --ink: #000000;
    --paper: #ffffff;
    --field-border: #9a9a9a;
    --headline-light: #d8d8d8;
    --headline-dark: #1c1c1c;
  }
  * { box-sizing: border-box; margin: 0; padding: 0; }
  html, body { width: 1200px; height: 771px; overflow: hidden; background: var(--ink); }
  .page {
    position: relative;
    width: 1200px;
    height: 771px;
    background: var(--ink);
    overflow: hidden;
    font-family: "Arimo", Arial, sans-serif;
  }
  .top-band {
    position: absolute;
    left: 0; top: 0;
    width: 1200px; height: 125px;
    background: var(--brand-red);
    display: flex;
    align-items: center;
    justify-content: center;
    gap: 12px;
  }
  .brand-mark {
    width: 34px; height: 34px;
    border: 3px solid var(--ink);
    border-radius: 50%;
  }
  .brand-name {
    font-size: 24px;
    font-weight: 700;
    color: var(--ink);
    letter-spacing: 1px;
  }
  .headline-art {
    position: absolute;
    left: 253px; top: 171px;
    width: 700px; height: 209px;
    background: radial-gradient(ellipse at center, var(--headline-light) 0%, #8a8a8a 45%, var(--headline-dark) 100%);
    border-radius: 40px;
  }
  .notify-form {
    position: absolute;
    left: 437px; top: 419px;
    display: flex;
    gap: 13px;
  }
  .notify-field {
    width: 251px; height: 41px;
    background: var(--ink);
    border: 2px solid var(--field-border);
    border-radius: 6px;
    box-shadow: 0 0 8px rgba(255,255,255,0.55);
    color: var(--paper);
    font: 400 15px "Arimo", Arial, sans-serif;
    padding: 0 10px;
    outline: none;
  }
  .notify-button {
    width: 99px; height: 41px;
    background: var(--accent-red);
    border: none;
    border-radius: 5px;
    color: var(--paper);
    font: 700 13px "Arimo", Arial, sans-serif;
  }
  .countdown {
    position: absolute;
    left: 0; top: 520px;
    width: 1200px;
    display: flex;
    justify-content: center;
    gap: 66px;
  }
  .countdown-unit {
    width: 134px; height: 134px;
    border: 4px solid var(--ring-red);
    border-radius: 50%;
    display: flex;
    align-items: center;
    justify-content: center;
    color: var(--paper);
    font-family: "Dancing Script", cursive;
    font-size: 24px;
  }
  .footer-wave {
    position: absolute;
    left: 0; top: 0;
    width: 1200px; height: 771px;
    pointer-events: none;
  }
  .social-links {
    position: absolute;
    left: 939px; top: 712px;
    display: flex;
    gap: 22px;
    list-style: none;
  }
  .social-link {
    width: 43px; height: 43px;
    border-radius: 50%;
    background: var(--ink);
    color: var(--paper);
    font-size: 9px;
    font-weight: 700;
    display: flex;
    align-items: center;
    justify-content: center;
  }
</style>
</head>
<body>
<main class="page">
  <header class="top-band">
    <span class="brand-mark"></span>
    <span class="brand-name">Darvelle</span>
  </header>

  <div class="headline-art" role="img" aria-label="Distressed white 'Coming soon' hand lettering with flowing swirl ornaments"></div>

  <form class="notify-form">
    <input class="notify-field" type="email" aria-label="Email address">
    <button class="notify-button" type="button">Get notified</button>
  </form>

  <section class="countdown">
    <div class="countdown-unit">10 days</div>
    <div class="countdown-unit">4 hours</div>
    <div class="countdown-unit">47 minutes</div>
    <div class="countdown-unit">11 seconds</div>
  </section>

  <svg class="footer-wave" viewBox="0 0 1200 771" aria-hidden="true">
    <path d="M640 771 C 820 720, 980 690, 1200 693 L 1200 771 Z" fill="#ffffff"/>
    <path d="M640 771 C 820 720, 980 690, 1200 693" fill="none" stroke="#d5101c" stroke-width="3"/>
  </svg>

  <ul class="social-links">
    <li class="social-link">Chirp</li>
    <li class="social-link">Facet</li>
    <li class="social-link">Plusly</li>
    <li class="social-link">Pinwall</li>
  </ul>
</main>
</body>
</html>
```